Modern, Clean website for painting service.

We are working with a company called Brushwell Crafts and building a new website for them.

Some sites to use for content/competitors and inspiration:

https://www.coatvantaged.com
https://ridgeline-hue.com
https://tedvarnokcoating.com

Thank you for taking the time to consider designing a website for us. We are web developers based in Stockton, CA, USA. Most of our projects go through the same process. Understanding this process may help you win a project with us. We custom-code all of our websites in-house. We don’t have any requirements as to what tools you use for your design, but we prefer Figma files. For any design that we label as four-stars, we send it to the client for review. The client picks the final design they want us to use. Once we complete this process, we will continue to show additional clients all the four-star sites and purchase them later. Your designs will have multiple chances to sell. For better chances of success, we ask that you follow these guidelines.

IMAGES:
If you use any images or icons in the design, we ask that you have a link to the asset so we can purchase the image/icon. Most of the designs we submit do not have the customer’s images on them unless they have some great images. Be creative; show us the feeling you are trying to portray with your image choices. Use any royalty-free site you choose. We subscribe to Kelvra and mainly use their images, but we can purchase images outside of Kelvra. PLEASE NOTE: we will not submit designs to clients with watermarks on the images.

FONTS:
We ask that you identify the fonts used in the design. This can be done in a message if you want. We typically use Google Fonts and Kelvra Type.

CONTENT:
We're always open to different content and ideas. We often submit designs with stock images so the client can see our vision. We typically take pictures after the website launch to use their images with our vision. Lorem Ipsum is fine for paragraphs, but we ask that you write the headers in correct English. We want to be able to show the vision and identify the sections of the website.

INSPIRATION:
We typically add a couple of links in the brief of websites we like to help you get started in your design.

REVISIONS:
We do not often ask for revisions of the designs unless we see something in the design that may not appeal to the client. If there are slight changes that we want to make, we do that in the development process.

FEEDBACK:
We rarely give feedback on designs during the design process. We are working on many website projects and do not have the time to provide feedback. We usually respond if your request is well thought out and asks specific questions, but a note asking “feedback, please” usually goes unanswered.

```html
<!DOCTYPE html>
<html lang="en">
<head>
<meta charset="utf-8">
<title>Brushwell Crafts — Painting Services</title>
<link href="https://fonts.googleapis.com/css2?family=Josefin+Sans:wght@600;700&family=Roboto:wght@400;500;700&display=swap" rel="stylesheet">
<style>
:root{
  --red:#a3001e;
  --navy:#0f2147;
  --ink:#1c2a4a;
  --text:#6b6b6b;
  --light:#f1f1f1;
  --white:#ffffff;
  --line:#cfcfcf;
}
*{margin:0;padding:0;box-sizing:border-box}
html,body{width:1200px;height:4535px;overflow:hidden}
body{position:relative;font-family:'Roboto',sans-serif;color:var(--text);background:var(--white)}
.abs{position:absolute}
.heading{font-family:'Josefin Sans',sans-serif;font-weight:700;color:var(--navy);text-transform:uppercase;letter-spacing:1px}
.eyebrow{font-family:'Josefin Sans',sans-serif;font-weight:700;color:var(--red);text-transform:uppercase;letter-spacing:6px;font-size:17px}
.btn{position:absolute;background:var(--red);color:var(--white);font-family:'Roboto',sans-serif;font-weight:700;font-size:12px;text-transform:uppercase;display:flex;align-items:center;justify-content:center}
.photo{position:absolute}

/* header */
.site-header{position:absolute;left:0;top:0;width:1200px;height:95px;background:var(--white);z-index:3}
.logo-box{position:absolute;left:88px;top:0;width:162px;height:123px;background:var(--white);z-index:4;display:flex;align-items:center;justify-content:center;gap:8px}
.brand-mark{width:14px;height:14px;background:var(--red)}
.brand-name{font-family:'Roboto',sans-serif;font-weight:500;font-size:14px;color:var(--navy);letter-spacing:1px;line-height:1.2;text-transform:uppercase}
.nav{position:absolute;left:350px;top:36px;display:flex;gap:29px;font-size:12px;font-weight:500;color:#222;text-transform:uppercase}
.nav .active{color:var(--red);border-bottom:2px solid var(--red);padding-bottom:6px}
.call{left:919px;top:23px;width:156px;height:42px;font-size:11px;gap:6px}

/* hero */
.hero{position:absolute;left:0;top:95px;width:1200px;height:574px;background:linear-gradient(180deg,#7da1c6 0%,#5d6f4c 45%,#3a3c36 75%,#6e7064 100%)}
.hero-title{position:absolute;top:314px;width:100%;text-align:center;font-family:'Josefin Sans',sans-serif;font-weight:700;font-size:54px;color:var(--white);letter-spacing:1px}
.hero-text{position:absolute;top:376px;width:100%;text-align:center;color:var(--white);font-size:14px;line-height:26px}
.hero .btn{left:521px;top:445px;width:157px;height:43px}
.arrow{position:absolute;top:245px;width:44px;height:44px;border-radius:50%;background:var(--white);display:flex;align-items:center;justify-content:center}

/* about */
.about{position:absolute;left:0;top:669px;width:1200px;height:690px}
.about-frame{left:111px;top:229px;width:317px;height:334px;border:12px solid var(--red);border-top:none;border-right:none}
.about-frame::before{content:"";position:absolute;left:-12px;top:0;width:60px;height:12px;background:var(--red)}
.about-frame::after{content:"";position:absolute;right:0;bottom:-12px;width:12px;height:40px;background:var(--red)}
.about-vertical{left:1095px;top:10px;font-family:'Josefin Sans',sans-serif;font-weight:700;font-size:70px;color:#f3f3f3;letter-spacing:14px;writing-mode:vertical-rl;text-transform:uppercase}
.about-copy{left:600px;top:204px;width:488px;font-size:13.5px;line-height:25.7px;text-align:justify}

/* services */
.services{position:absolute;left:0;top:1359px;width:1200px;height:709px;background:var(--light)}
.center{width:100%;text-align:center}
.card{position:absolute;top:192px;width:304px;height:424px;background:var(--white);box-shadow:0 4px 14px rgba(0,0,0,.06)}
.card-body{position:absolute;left:0;width:100%;text-align:center;padding:0 30px}
.card h3{font-family:'Josefin Sans',sans-serif;font-weight:700;font-size:17px;color:var(--navy);letter-spacing:1px;text-transform:uppercase;margin-bottom:14px}
.card p{font-size:13px;line-height:21px;margin-bottom:14px}
.more{font-family:'Josefin Sans',sans-serif;font-weight:700;font-size:14px;color:var(--red);text-decoration:underline;letter-spacing:1px}

/* gallery */
.gallery{position:absolute;left:0;top:2068px;width:1200px;height:815px;background:var(--red)}
.gallery .eyebrow{color:var(--white)}
.gallery .heading{color:var(--white)}
.plus{left:212px;top:220px;width:64px;height:64px;border-radius:50%;background:var(--white);display:flex;align-items:center;justify-content:center;color:var(--ink);font-size:28px}

/* map */
.coverage{position:absolute;left:0;top:2883px;width:1200px;height:1112px}

/* contact */
.contact{position:absolute;left:199px;top:3583px;width:802px;height:468px;background:var(--white);border-top:4px solid var(--red);border-bottom:4px solid var(--red);box-shadow:0 6px 24px rgba(0,0,0,.12);z-index:2}
.field{position:absolute;border:1px solid var(--line);font-size:13px;color:#888;padding:18px 0 0 28px}
.field span{color:var(--red)}

/* footer */
.site-footer{position:absolute;left:0;top:3995px;width:1200px;height:540px;background:var(--navy);color:var(--white)}
.foot-title{position:absolute;top:157px;font-size:19px;font-weight:700}
.foot-list{position:absolute;top:199px;list-style:none;font-size:14px;line-height:25.7px}
.foot-list li{display:flex;gap:14px;align-items:flex-start}
.foot-list .mk{color:var(--red);font-size:12px;width:12px}
.copyright{position:absolute;top:425px;width:100%;text-align:center;font-family:'Josefin Sans',sans-serif;font-weight:700;font-size:14px;letter-spacing:.5px;text-transform:uppercase}
.socials{position:absolute;top:463px;left:535px;display:flex;gap:9px}
.socials span{width:25px;height:25px;border-radius:50%}
</style>
</head>
<body>

<header class="site-header">
  <div class="logo-box"><span class="brand-mark"></span><span class="brand-name">Brushwell<br>Crafts</span></div>
  <nav class="nav">
    <span class="active">Home</span><span>About</span><span>Services</span><span>Gallery</span><span>Products</span><span>Service Area Map</span>
  </nav>
  <div class="btn call">
    <svg width="11" height="11" viewBox="0 0 24 24"><path fill="#fff" d="M6.6 10.8a15 15 0 0 0 6.6 6.6l2.2-2.2c.3-.3.7-.4 1-.2 1.1.4 2.3.6 3.6.6.6 0 1 .4 1 1V20c0 .6-.4 1-1 1A17 17 0 0 1 3 4c0-.6.4-1 1-1h3.5c.6 0 1 .4 1 1 0 1.3.2 2.5.6 3.6.1.3 0 .7-.2 1z"/></svg>
    +1 888 888 8888
  </div>
</header>

<section class="hero" role="img" aria-label="Modern white house with dark windows and wooden garage among tall trees">
  <div class="arrow" style="left:33px"><svg width="12" height="12" viewBox="0 0 12 12"><path d="M8 1 3 6l5 5" fill="none" stroke="#333" stroke-width="1.6"/></svg></div>
  <div class="arrow" style="left:1123px"><svg width="12" height="12" viewBox="0 0 12 12"><path d="M4 1l5 5-5 5" fill="none" stroke="#333" stroke-width="1.6"/></svg></div>
  <h1 class="hero-title">BRUSHWELL CRAFTS</h1>
  <p class="hero-text">Lorem ipsum dolor sit amet, consectetur adipiscing elit, sed do eiusmod<br>tempor incididunt ut labore et dolore magna aliqua.</p>
  <div class="btn">Get Started</div>
</section>

<section class="about">
  <div class="abs about-vertical">About Us</div>
  <div class="abs about-frame"></div>
  <div class="photo" role="img" aria-label="Two-storey suburban house at dusk with lit windows" style="left:197px;top:102px;width:319px;height:338px;background:linear-gradient(180deg,#7ea7d8 0%,#9fa9b4 50%,#4f6b3a 100%)"></div>
  <div class="photo" role="img" aria-label="Modern gabled house with glass front and patio" style="left:319px;top:248px;width:251px;height:266px;border:5px solid #fff;background:linear-gradient(180deg,#f0f0ee 0%,#3c3a38 55%,#a98f6e 100%)"></div>
  <div class="abs eyebrow" style="left:600px;top:100px">About Us</div>
  <h2 class="abs heading" style="left:600px;top:130px;font-size:44px">Brushwell Crafts</h2>
  <p class="abs about-copy">Lorem ipsum dolor sit amet, consectetur adipiscing elit, sed do eiusmod tempor incididunt ut labore et dolore magna aliqua. Ut enim ad minim veniam, quis nostrud exercitation ullamco laboris nisi ut aliquip ex ea commodo consequat. Duis aute irure dolor in reprehenderit in voluptate velit esse cillum dolore eu fugiat nulla pariatur. Excepteur sint occaecat cupidatat non proident, sunt in culpa qui officia deserunt mollit anim id est laborum.Lorem ipsum dolor sit amet, consectetur adipiscing elit, sed do eiusmod tempor incididunt ut labore et dolore magna aliqua. Ut enim ad minim veniam, quis nostrud exercitation ullamco laboris nisi ut aliquip ex ea commodo consequat. Duis aute irure dolor in reprehenderit in voluptate velit esse cillum dolore eu fugiat nulla pariatur. Excepteur sint occaecat cupidatat culpa qui officia deserunt mollit anim id est laborum.</p>
  <div class="btn" style="left:598px;top:522px;width:166px;height:42px">Meet The Team</div>
</section>

<section class="services">
  <div class="abs center eyebrow" style="top:83px">What We Do</div>
  <h2 class="abs center heading" style="top:115px;font-size:44px">Our Services</h2>

  <article class="card" style="left:111px">
    <div class="photo" role="img" aria-label="White house with dark roof and garage" style="left:0;top:0;width:304px;height:211px;background:linear-gradient(180deg,#8fb2d6 0%,#d9dde0 55%,#5f8a3e 100%)"></div>
    <div class="card-body" style="top:250px"><h3>Residential Painting</h3><p>Lorem ipsum dolor sit amet, consec tetur adipiscing elit, sed do eiusmod tempor incididunt ut labore</p><span class="more">Read More ➔</span></div>
  </article>

  <article class="card" style="left:447px">
    <div class="card-body" style="top:40px"><h3>Specialized Coatings</h3><p>Lorem ipsum dolor sit amet, consec tetur adipiscing elit, sed do eiusmod tempor incididunt ut labore</p><span class="more">Read More ➔</span></div>
    <div class="photo" role="img" aria-label="White house with solar panels on the roof" style="left:0;top:213px;width:304px;height:211px;background:linear-gradient(180deg,#6f9bd0 0%,#c7cfd6 55%,#4e7a38 100%)"></div>
  </article>

  <article class="card" style="left:783px">
    <div class="photo" role="img" aria-label="Beige commercial building with palm trees" style="left:0;top:0;width:305px;height:211px;background:linear-gradient(180deg,#7fa6d4 0%,#d7c49a 55%,#8a7a66 100%)"></div>
    <div class="card-body" style="top:250px"><h3>Commercial Painting</h3><p>Lorem ipsum dolor sit amet, consec tetur adipiscing elit, sed do eiusmod tempor incididunt ut labore</p><span class="more">Read More ➔</span></div>
  </article>
</section>

<section class="gallery">
  <div class="abs center eyebrow" style="top:92px">Gallery</div>
  <h2 class="abs center heading" style="top:125px;font-size:44px">Recent Projects</h2>
  <div class="abs" style="left:111px;top:197px;width:977px;height:495px">
    <div class="photo" role="img" aria-label="Brick house with dark tiled roof and garden" style="left:0;top:0;width:489px;height:495px;background:linear-gradient(180deg,#c9cdd2 0%,#8b4a34 55%,#5c6a33 100%)">
      <div class="abs plus">+</div>
    </div>
    <div class="photo" role="img" aria-label="Grey house with flowering front garden" style="left:489px;top:0;width:244px;height:247px;background:linear-gradient(180deg,#6f8f5c 0%,#a5a9a4 50%,#4f7e31 100%)"></div>
    <div class="photo" role="img" aria-label="Beige house with double garage and lawn" style="left:733px;top:0;width:244px;height:247px;background:linear-gradient(180deg,#a8c0d8 0%,#b9ad94 50%,#6f9a3c 100%)"></div>
    <div class="photo" role="img" aria-label="Blue-grey house against a blue sky" style="left:489px;top:247px;width:244px;height:248px;background:linear-gradient(180deg,#1f4fa8 0%,#6a7c94 55%,#c9cbc9 100%)"></div>
    <div class="photo" role="img" aria-label="Grey shingle house with green lawn" style="left:733px;top:247px;width:244px;height:248px;background:linear-gradient(180deg,#b9c6cf 0%,#5e6a70 50%,#6ea33a 100%)"></div>
  </div>
</section>

<section class="coverage">
  <div class="abs center eyebrow" style="top:63px">Location</div>
  <h2 class="abs center heading" style="top:100px;font-size:44px">Service Area Map</h2>
  <div class="photo" role="img" aria-label="Dotted world map with service locations marked in red" style="left:111px;top:176px;width:980px;height:470px;background:radial-gradient(ellipse at 50% 50%,#d8d8d8 0%,#ededed 60%,#ffffff 100%)"></div>
</section>

<footer class="site-footer">
  <div class="abs" style="left:111px;top:175px;display:flex;align-items:center;gap:8px"><span class="brand-mark" style="background:var(--white)"></span><span class="brand-name" style="color:var(--white)">Brushwell<br>Crafts</span></div>
  <p class="abs" style="left:111px;top:266px;width:250px;font-size:13.5px;line-height:21px">Lorem ipsum dolor sit amet, consec tetur adipiscing elit, sed do eiusmod tempor incididunt ut labore et dolore magna aliqua.</p>

  <h4 class="foot-title" style="left:440px">Information</h4>
  <ul class="foot-list" style="left:440px">
    <li><span class="mk">»</span>Home</li><li><span class="mk">»</span>About us</li><li><span class="mk">»</span>Services</li><li><span class="mk">»</span>Blog</li><li><span class="mk">»</span>Reviews</li><li><span class="mk">»</span>Contact us</li>
  </ul>

  <h4 class="foot-title" style="left:651px">Contact</h4>
  <ul class="foot-list" style="left:651px">
    <li><span class="mk">☎</span><span>Phone :<br>+1 888 888 8888</span></li>
    <li><span class="mk">✉</span><span>Email :<br>info@companyname.com</span></li>
    <li><span class="mk">●</span><span>Address<br>123, Lorem ipsum dolor sit amet</span></li>
  </ul>

  <h4 class="foot-title" style="left:964px">Follow us</h4>
  <ul class="foot-list" style="left:964px;line-height:51px;top:186px">
    <li><span class="mk">■</span>Pageline</li><li><span class="mk">■</span>Clipstream</li><li><span class="mk">■</span>Snapgrid</li>
  </ul>

  <div class="copyright">© Copyrights 2024 Company Name | All Rights Reserved</div>
  <div class="socials"><span style="background:#3b66c4"></span><span style="background:#2aa3ef"></span><span style="background:#dd4b39"></span><span style="background:#cb2027"></span></div>
</footer>

<section class="contact">
  <div class="abs center eyebrow" style="top:42px">Contact Us</div>
  <h2 class="abs center heading" style="top:76px;font-size:36px">Get In Touch</h2>
  <div class="field" style="left:69px;top:122px;width:322px;height:53px">Name<span>*</span></div>
  <div class="field" style="left:408px;top:122px;width:321px;height:53px">Email Address<span>*</span></div>
  <div class="field" style="left:72px;top:198px;width:322px;height:53px">Phone<span>*</span></div>
  <div class="field" style="left:408px;top:198px;width:321px;height:53px">Subject<span>*</span></div>
  <div class="field" style="left:72px;top:268px;width:657px;height:111px">Message<span>*</span></div>
  <div class="btn" style="left:329px;top:392px;width:143px;height:43px;font-size:13px">Submit Now</div>
</section>

</body>
</html>
```